Schnapsbrennerei sucht neue Etiketten
Zielgruppe
Wir sind eine örtliche Schnapsbrennerei, die inzwischen seit ein paar Jahren einen eigenen Kundenstamm aufgebaut hat. Nun werden wir im nächsten Jahr einen neuen Verkaufsraum bauen. Aus diesem Grund wollen wir unsere Etiketten komplett überarbeiten.
Ein neues Logo habe ich bereits designen lassen. Diese finden Sie unten im Dokumententenupload. Wir legen viel Wert auf eine sehr hohe Qualität, welche sich sowohl in unserem Logo als auch den Etiketten Wiederspiegeln soll.
Unsere Kundschaft ist hauptsächlich Ü35 und legt viel Wert auf hochwertige Produkte.
Aufgabenstellung
Eines direkt vorne weg: Da wir unsere komplette Produktpalette neu gestalten wollen würde ich Sie bitten, der Einfachheit halber zuerst nur ein Schnapsetikett (z.B. Zwetschge oder Willi), ein Likör Etikett und ein Etikett für unseren Whiskey zu erstellen.
Darüber hinaus bitte ich Sie auch ein Design für unseren neuen Gin und einen Aquavit, welcher im Herbst auf den Markt kommen soll zu designen. Im Anschluss daran, werde ich in der Zusammenarbeit mit Ihnen die Etiketten optimieren wollen.
Sobald ein 'Grundetikett' entstanden ist, sollen dann auch die anderen Schnäpse und Liköre in dem gleichen Stil erstellt werden. Explizit möchte ich daraufhin weisen, dass sowohl die Whiskeys als auch der Gin und der Aquavit nicht zwangsläufig das gleiche 'Grundetikett' wie der Schnaps und der Likör haben sollen. Ist bei unseren aktuellen Etiketten auch nicht der Fall. Sehen Sie in den Bildern unten.
Wir verkaufen unseren Schnaps und Likör in 3 unterschieldichen Größen 0,2; 0,5 und 1,0 Liter. Wir verwenden für die 0,2 und 0,5 die Flasche Lumbra. Das Etikett der 0,5er Flasche soll in etwa 65x120-130 mm sein. Hier sind wir allerdings variabel.
Dieses entstandene Etikett soll dann auf die anderen Flaschen entsprechend angepasst werden.
Sie finden im Dokumentenupload unsere aktuellen Etiketten und das Logo, welches eingebaut werden soll. Auch ein Etikett von einem örtlichen Weingut, welches mir vom Aufbau und der Unterteilung sehr gut gefällt, werde ich mit anhängen. Allerdings ist dieses Bild sehr unscharf. Wie gesagt es geht hierbei hauptsächlich um die Einteilung mit den oberen und den unteren 'Rahmen'.
Auch unsere Preisliste finden Sie Anhang, wobei diese noch in der Rohform ist und das Obst so nicht verwendet wird, aber hier sind die meisten Produkte drauf.
Das Logo gibt es in verschiedenen Farben. Gerne dürfen Sie für die unterschiedlichen Produkte auch unterschiedliche Farben nutzen.
Was ich mir persönlich g..

```html
<!DOCTYPE html>
<html lang="de">
<head>
<meta charset="utf-8">
<title>Whiskey Etikett – Hallinger's Landbrennerei</title>
<link rel="stylesheet" href="https://fonts.googleapis.com/css2?family=Montserrat:wght@400;500;700;800&family=Josefin+Sans:wght@100;200&display=swap">
<style>
  :root {
    --backdrop: #b3b3b3;
    --paper: #ffffff;
    --ink: #1c1c1c;
    --amber: #e39b26;
    --glass-light: #f1ede8;
    --whiskey: #dca27a;
    --whiskey-deep: #c98a63;
  }
  * { margin: 0; padding: 0; box-sizing: border-box; }
  html, body {
    width: 1200px; height: 2400px; overflow: hidden;
    background: var(--backdrop);
  }
  .canvas { position: relative; width: 1200px; height: 2400px; }
  .label {
    position: absolute; left: 97px; top: 271px;
    width: 1006px; height: 1857px;
    background: var(--paper);
    color: var(--ink);
    font-family: "Montserrat", sans-serif;
  }
  .label > * { position: absolute; }
  .tagline {
    top: 46px; left: 95px; width: 814px;
    font-size: 27px; font-weight: 400; letter-spacing: 24px;
    white-space: nowrap;
  }
  .brand-dot {
    top: 170px; left: 453px; width: 100px; height: 100px;
    border-radius: 50%; background: var(--amber);
  }
  .brand-rule { top: 390px; height: 2px; width: 200px; background: var(--ink); }
  .brand-rule--left { left: 104px; }
  .brand-rule--right { left: 702px; }
  .brand-name {
    top: 408px; left: 0; width: 100%; text-align: center;
    font-size: 52px; font-weight: 700; letter-spacing: 10px;
  }
  .brand-sub {
    top: 478px; left: 0; width: 100%; text-align: center;
    font-size: 21px; font-weight: 700; letter-spacing: 9px;
  }
  .serving-art {
    top: 640px; left: 211px; width: 597px; height: 752px;
    border-radius: 30px 30px 60px 60px;
    background: linear-gradient(180deg, var(--glass-light) 0%, var(--glass-light) 30%,
      var(--whiskey) 45%, var(--whiskey-deep) 68%, var(--glass-light) 82%, #e4e1dd 100%);
  }
  .product-name {
    top: 1394px; left: 92px; width: 820px;
    font-size: 138px; font-weight: 800; letter-spacing: 14px; line-height: 1;
    white-space: nowrap;
  }
  .double-rule { height: 8px; border-top: 3px solid var(--ink); border-bottom: 2px solid var(--ink); }
  .double-rule--wide { top: 1570px; left: 95px; width: 807px; }
  .double-rule--short { top: 1775px; left: 95px; width: 533px; }
  .origin {
    top: 1612px; left: 95px;
    font-size: 28px; font-weight: 500; letter-spacing: 3px; white-space: nowrap;
  }
  .maker {
    top: 1672px; left: 95px;
    font-size: 19px; font-weight: 400; letter-spacing: 2.5px; line-height: 22px;
    text-transform: uppercase;
  }
  .volume {
    top: 1712px; left: 532px;
    font-family: "Josefin Sans", sans-serif; font-weight: 200;
    font-size: 46px; color: var(--amber); white-space: nowrap;
  }
  .strength {
    top: 1612px; left: 692px;
    font-family: "Josefin Sans", sans-serif; font-weight: 100;
    font-size: 178px; line-height: 1; color: var(--amber);
  }
  .strength sup { font-size: 64px; vertical-align: 92px; margin-left: 6px; }
  .lot {
    top: 1760px; left: 692px;
    font-size: 19px; letter-spacing: 6px; white-space: nowrap;
  }
  .lot strong { font-weight: 500; margin-left: 18px; }
</style>
</head>
<body>
<main class="canvas">
  <article class="label">
    <p class="tagline">IM HOLZFASS GEREIFT</p>
    <span class="brand-dot"></span>
    <span class="brand-rule brand-rule--left"></span>
    <span class="brand-rule brand-rule--right"></span>
    <p class="brand-name">HALLINGER'S</p>
    <p class="brand-sub">LANDBRENNEREI</p>
    <div class="serving-art" role="img" aria-label="Aquarellzeichnung eines Whiskeyglases mit Eiswürfeln"></div>
    <h1 class="product-name">WHISKEY</h1>
    <span class="double-rule double-rule--wide"></span>
    <p class="origin">HERGESTELLT IN DEUTSCHLAND</p>
    <p class="maker">Edelbrände &amp; Liköre Gerd Hallinger<br>Lindenweg 12<br>D-96123 Talbach<br>09471 - 38 52</p>
    <p class="volume">0,5 L</p>
    <span class="double-rule double-rule--short"></span>
    <p class="strength">40<sup>%</sup></p>
    <p class="lot">L.-NR.<strong>11/10</strong></p>
  </article>
</main>
</body>
</html>
```